Web Design Project

The aim of this project to design a website for a service that would offer services for small business and non profit organizations using opensource software that is weaved to work together in harmony.

The website name is: velisto.net

Tavrel in Arabic means: cabbage. Cabbage is composed of leaves, actually there is nothing except leaves. Each leave by itself is not called cabbage, but a collection of leaves that are organized in a central way would give us cabbage.

Same idea for Tavrel where open source software very well organized and integrated would create a new thing with a new value.
Updates

Target Market(s)

Small business, Europe, Africa, Far east and Middle east

Industry/Entity Type

Small Business

Requirements
Must have
• The website would offer the following sections:
* Home page
* Benefits: value of tavrel
* Applications: applications offered by tavrel
* Pricing
* Purchase
* Customer log in
* Support
- FAQ
- Knowledge base
- Forums
- Open tickets

Please take the following consideration in design:
* White should predominate
* Only black and the colors of logo are permitted (attched)
Nice to have
• Design is better to express:
* Openness
* Dynamic
* Usable
* Cost effective

```html
<!DOCTYPE html>
<html lang="en">
<head>
<meta charset="utf-8">
<title>Tavrel — open source, woven together</title>
<link rel="stylesheet" href="https://fonts.googleapis.com/css2?family=Open+Sans:wght@300;400;600;700&display=swap">
<style>
:root{
  --green:#7ac143;
  --yellow:#f5b800;
  --blue:#1a8fd8;
  --ink:#222;
  --text:#555;
  --muted:#8a8a8a;
  --paper:#fafafa;
  --band:#efefef;
  --footer:#333;
  --footer-bar:#1b1b1b;
  --white:#fff;
}
*{margin:0;padding:0;box-sizing:border-box}
html,body{width:689px;height:1200px;overflow:hidden}
body{position:relative;background:var(--paper);font-family:"Open Sans",Arial,sans-serif;color:var(--text)}
.abs{position:absolute}

/* header */
.site-header{position:absolute;left:0;top:0;width:689px;height:67px;background:var(--white)}
.brand{left:93px;top:12px;display:flex;align-items:center;gap:8px}
.brand-dot{width:34px;height:34px;border-radius:50%;background:var(--green)}
.brand-name{font-size:28px;font-weight:600;color:var(--ink);letter-spacing:-.5px}
.main-nav{left:331px;top:40px;display:flex;gap:14px;font-size:9.5px;font-weight:600;color:var(--ink)}
.main-nav a{color:inherit;text-decoration:none;line-height:16px}
.main-nav .active{background:var(--green);color:var(--white);padding:0 9px;border-radius:3px}
.login{left:503px;top:17px;width:42px;height:14px;border-radius:3px;background:var(--yellow);color:var(--white);font-size:7.5px;font-weight:700;text-align:center;line-height:14px}
.social-top{left:558px;top:20px;display:flex;gap:6px}
.social-top span{width:8px;height:8px;background:#666;border-radius:1px}

/* hero */
.hero{left:0;top:67px;width:689px;height:248px;background:linear-gradient(100deg,#2b2620 0%,#4a3b2b 45%,#6a5540 70%,#3a3128 100%)}
.hero-copy{left:101px;top:129px;width:250px}
.hero-copy h1{font-size:19.5px;font-weight:400;line-height:22.5px}
.hero-copy .g{color:var(--green)}
.hero-copy .y{color:var(--yellow);font-weight:600}
.hero-copy p{margin-top:9px;font-size:8.5px;line-height:11px;color:#e8e2d8}
.hero-arrow{top:178px;width:30px;height:30px;border-radius:50%;background:rgba(255,255,255,.55);z-index:2}
.hero-visual{left:377px;top:109px;width:216px;height:200px;border-radius:6px;background:linear-gradient(160deg,#f4f4f4,#cfcfcf 70%,#9a9a9a)}

/* partners */
.partners{left:0;top:315px;width:689px;height:72px;background:var(--band);border-bottom:1px solid #e0e0e0}
.partner{top:333px;height:36px;background:#9a9a9a;opacity:.75}

/* features */
.section-title{left:0;width:689px;text-align:center;font-weight:300;color:var(--ink)}
.section-sub{left:0;width:689px;text-align:center;font-size:9px;color:var(--muted)}
.feature{top:474px;width:160px;text-align:center}
.feature-icon{width:74px;height:74px;border-radius:50%;margin:0 auto;display:flex;align-items:center;justify-content:center}
.feature h3{margin-top:6px;font-size:14px;font-weight:400;color:var(--ink)}
.feature p{margin-top:5px;font-size:7.5px;line-height:10px;color:var(--muted)}

/* promo band */
.promo{left:0;top:637px;width:689px;height:200px;background:linear-gradient(110deg,#6b3a86 0%,#8a4d86 30%,#5a5f95 60%,#2d8a96 100%)}
.promo-copy{left:93px;top:685px;width:240px;color:var(--white)}
.promo-copy h2{font-size:12.5px;font-weight:400;color:var(--yellow)}
.promo-copy p{margin-top:5px;font-size:8.5px;line-height:10.5px;font-weight:700}
.ticks{margin-top:7px;display:grid;grid-template-columns:94px 110px;row-gap:5px;font-size:8.5px}
.ticks li{list-style:none;display:flex;gap:4px;align-items:center}
.promo-visual{left:344px;top:668px;width:256px;height:162px;border-radius:8px;background:linear-gradient(135deg,rgba(255,255,255,.85),rgba(220,230,235,.6))}

/* testimonials */
.testimonial{display:flex;gap:16px;align-items:flex-start}
.avatar{flex:none;width:56px;height:56px;border-radius:50%;background:linear-gradient(160deg,#c9d7e3,#8aa0b5);border:2px solid var(--white)}
.quote{position:relative;width:180px;padding:4px 14px 0 14px}
.quote-text{font-size:7.5px;line-height:10px;color:var(--muted)}
.quote-mark{position:absolute;font-size:20px;line-height:20px;color:#c8c8c8;font-family:Georgia,serif}
.quote-mark.open{left:0;top:0}
.quote-mark.close{right:0;top:22px}
.quote-link{margin-top:7px;font-size:8.5px;color:var(--blue)}

/* footer */
.site-footer{left:0;top:1061px;width:689px;height:112px;background:var(--footer)}
.footer-col h4{font-size:9px;font-weight:700;color:var(--yellow)}
.footer-col p,.footer-col li{font-size:7.5px;line-height:10px;color:#888;list-style:none}
.newsletter{left:461px;top:1081px;width:115px;height:20px;background:var(--white);border-radius:2px;font-size:8px;color:#777;padding:4px 6px}
.office{left:461px;top:1106px;font-size:8px;line-height:13px;color:var(--white)}
.social-foot{left:461px;top:1145px;display:flex;gap:3px}
.social-foot span{width:14px;height:14px;border-radius:2px}
.tweet-link{left:313px;top:1134px;width:70px;height:14px;border:1px solid #aaa;font-size:7px;color:var(--white);padding:1px 4px}
.footer-bar{left:0;top:1173px;width:689px;height:27px;background:var(--footer-bar);font-size:7.5px;color:var(--white)}
.footer-bar .copy{position:absolute;left:103px;top:9px}
.footer-bar nav{position:absolute;right:98px;top:9px;display:flex;gap:13px}
</style>
</head>
<body>

<header class="site-header">
  <div class="brand abs"><span class="brand-dot"></span><span class="brand-name">tavrel</span></div>
  <div class="login abs">LOGIN</div>
  <div class="social-top abs"><span></span><span></span><span></span></div>
  <nav class="main-nav abs">
    <a class="active">Benefits</a><a>Applications</a><a>Pricing</a><a>Purchase</a><a>Support ▾</a>
  </nav>
</header>

<section class="hero abs" role="img" aria-label="Blurred office photograph behind the slider"></section>
<div class="hero-visual abs" role="img" aria-label="Desktop monitor showing the Tavrel website with a round Tavrel badge in front"></div>
<div class="hero-arrow abs" style="left:54px"></div>
<div class="hero-arrow abs" style="left:606px"></div>
<div class="hero-copy abs">
  <h1><span class="g">Duis autem vel eum iriure</span><br><span class="y">Processus dynamicus</span><br><span class="g">Mirum est notare</span></h1>
  <p>Lorem ipsum dolor sit amet, consectetuer adipiscing elit, sed diam nonummy nibh euismod tincidunt ut laoreet dolore magna aliquam erat volutpat. Ut wisi enim ad minim veniam, quis nostrud exerci tation ullamcorper suscipit lobortis nisl ut aliquip ex ea commodo consequat.</p>
</div>

<section class="partners abs" aria-label="Partners"></section>
<div class="partner abs" style="left:112px;width:110px"></div>
<div class="partner abs" style="left:264px;width:50px;border-radius:50%"></div>
<div class="partner abs" style="left:356px;width:36px;border-radius:50% 50% 50% 50%/60% 60% 40% 40%"></div>
<div class="partner abs" style="left:434px;width:80px"></div>
<div class="partner abs" style="left:537px;width:40px;border-radius:50%"></div>

<h2 class="section-title abs" style="top:404px;font-size:28px">Lorem ipsum dolor sit amet</h2>
<p class="section-sub abs" style="top:440px">Ut wisi enim ad minim veniam, quis nostrud exerci tation</p>

<div class="feature abs" style="left:87px">
  <div class="feature-icon" style="background:var(--yellow)">
    <svg width="30" height="36" viewBox="0 0 30 36"><path d="M2 2h18l8 8v24H2z" fill="#fff"/><rect x="7" y="22" width="4" height="8" fill="#f5b800"/><rect x="13" y="17" width="4" height="13" fill="#f5b800"/><rect x="19" y="12" width="4" height="18" fill="#f5b800"/></svg>
  </div>
  <h3>Benefits</h3>
  <p>Duis autem vel eum iriure dolor est etiam in velit esse molestie consequat, vel illum dolore eu feugiat nulla facilisis at vero eros.</p>
</div>
<div class="feature abs" style="left:265px">
  <div class="feature-icon" style="background:var(--blue)">
    <svg width="34" height="34" viewBox="0 0 34 34"><rect x="3" y="3" width="12" height="12" rx="2" fill="#fff"/><rect x="19" y="3" width="12" height="12" rx="2" fill="#fff"/><rect x="3" y="19" width="12" height="12" rx="2" fill="#fff"/><rect x="19" y="19" width="12" height="12" rx="2" fill="#fff"/></svg>
  </div>
  <h3>Applications</h3>
  <p>Duis autem vel eum iriure dolor est etiam in velit esse molestie consequat, vel illum dolore eu feugiat nulla facilisis at vero eros.</p>
</div>
<div class="feature abs" style="left:439px">
  <div class="feature-icon" style="background:var(--green)">
    <svg width="28" height="36" viewBox="0 0 28 36"><rect x="1" y="1" width="26" height="34" rx="3" fill="#fff"/><rect x="5" y="5" width="18" height="7" fill="#7ac143"/><g fill="#7ac143"><rect x="5" y="15" width="5" height="4"/><rect x="12" y="15" width="5" height="4"/><rect x="19" y="15" width="4" height="4"/><rect x="5" y="22" width="5" height="4"/><rect x="12" y="22" width="5" height="4"/><rect x="19" y="22" width="4" height="4"/><rect x="5" y="29" width="5" height="3"/><rect x="12" y="29" width="5" height="3"/><rect x="19" y="29" width="4" height="3"/></g></svg>
  </div>
  <h3>Pricing</h3>
  <p>Duis autem vel eum iriure dolor est etiam in velit esse molestie consequat, vel illum dolore eu feugiat nulla facilisis at vero eros.</p>
</div>

<section class="promo abs"></section>
<svg class="abs" style="left:335px;top:637px" width="20" height="10"><path d="M0 0h20L10 10z" fill="#fafafa"/></svg>
<svg class="abs" style="left:335px;top:837px" width="20" height="8"><path d="M0 0h20L10 8z" fill="#5a5f95"/></svg>
<div class="promo-copy abs">
  <h2>Claritas est etiam processus</h2>
  <p>Autem vel eum iriure dolor in hendrerit in vulputate velit esse molestie consequat, vel sequitur mutationem illum dolore eu feugiat nulla.</p>
  <ul class="ticks">
    <li>✔ Duis autem vel eum</li><li>✔ Ut wisi enim ad</li>
    <li>✔ Nam liber tempor</li><li>✔ Lorem ipsum dolor</li>
  </ul>
</div>
<div class="promo-visual abs" role="img" aria-label="Screenshot of the customer dashboard with round callouts for mobile app download and social connect"></div>

<h2 class="section-title abs" style="top:850px;font-size:27px">What Our Customers Are Saying</h2>

<div class="testimonial abs" style="left:93px;top:893px">
  <div class="avatar" role="img" aria-label="Customer portrait"></div>
  <div class="quote"><span class="quote-mark open">“</span><p class="quote-text">Autem vel eum iriure dolor in hendrerit in vulputate velit esse molestie consequat, vel sequitur mutationem illum dolore eu feugiat nulla olestie.</p><span class="quote-mark close">”</span><p class="quote-link">Ut wisi enim ad minim veniam</p></div>
</div>
<div class="testimonial abs" style="left:357px;top:893px">
  <div class="avatar" role="img" aria-label="Customer portrait"></div>
  <div class="quote"><span class="quote-mark open">“</span><p class="quote-text">Autem vel eum iriure dolor in hendrerit in vulputate velit esse molestie consequat, vel sequitur mutationem illum dolore eu feugiat nulla olestie.</p><span class="quote-mark close">”</span><p class="quote-link">Ut wisi enim ad minim veniam</p></div>
</div>
<div class="testimonial abs" style="left:93px;top:980px">
  <div class="avatar" role="img" aria-label="Customer portrait"></div>
  <div class="quote"><span class="quote-mark open">“</span><p class="quote-text">Autem vel eum iriure dolor in hendrerit in vulputate velit esse molestie consequat, vel sequitur mutationem illum dolore eu feugiat nulla olestie.</p><span class="quote-mark close">”</span><p class="quote-link">Ut wisi enim ad minim veniam</p></div>
</div>
<div class="testimonial abs" style="left:357px;top:980px">
  <div class="avatar" role="img" aria-label="Customer portrait"></div>
  <div class="quote"><span class="quote-mark open">“</span><p class="quote-text">Autem vel eum iriure dolor in hendrerit in vulputate velit esse molestie consequat, vel sequitur mutationem illum dolore eu feugiat nulla olestie.</p><span class="quote-mark close">”</span><p class="quote-link">Ut wisi enim ad minim veniam</p></div>
</div>

<footer class="site-footer abs"></footer>
<div class="footer-col abs" style="left:93px;top:1078px;width:105px">
  <h4>About Tavrel</h4>
  <p style="margin-top:6px">Lorem ipsum dolor sit amet, consectetuer adipiscing elit, sed diam nonummy nibh euismod tincidunt ut laoreet dolore magna aliquam erat volutpat.</p>
</div>
<div class="footer-col abs" style="left:223px;top:1078px">
  <h4>AX SERVICES</h4>
  <ul style="margin-top:6px"><li>FAQ</li><li>Knowledge base</li><li>Forums</li><li>Open tickets</li></ul>
</div>
<div class="footer-col abs" style="left:313px;top:1078px;width:120px">
  <h4>LATEST POSTS</h4>
  <p style="margin-top:6px">Lorem ipsum dolor sit amet, consectetuer adipiscing elit, sed diam nonummy nibh ut laoreet</p>
</div>
<div class="tweet-link abs">http://t.co/x7Lm2Q</div>
<div class="newsletter abs">Newsletter</div>
<div class="office abs">Office in Europe<br>+12-34-555-0142<br>Netherlands, Haarlem</div>
<div class="social-foot abs"><span style="background:#3b5a9a"></span><span style="background:#2aa6de"></span><span style="background:#d23b2f"></span></div>

<div class="footer-bar abs">
  <span class="copy">© 2014 velisto.net All Right Reserved</span>
  <nav><span>Benefits</span><span>Applications</span><span>Pricing</span><span>Purchase</span><span>Support</span></nav>
</div>

</body>
</html>
```